Electrical Contractors Business Card Design

I need a business card design for an electrical contracting business. A theme I was thinking of is the BE of Brightway Electrical both facing each other ie the second E is back to front and maybe each horizontal part of the E's are a different colours of the internal wires of TPS cable. The top would be blue(representing the sky), the middle green(representing the grass) and the lower would be brown(representing below the earth) (neutral,earth and active). And coming out of the back of each E going to each side of the business card would be the white outer sheath of TPS cable. I would like a big part of the card to be a very bright emerald flourescent green and maybe silver for the top half. the message I would like to send is that of an environmentally friendly, ethical business that delivers quality sevice on time.

Target Market(s)

40 to 80 year old home owners

Industry/Entity Type

Electrical

Contact Information for Business Card

Tom Keller
Brightway Electrical
EC 274381
Mob: 0417 592 064

```html
<!DOCTYPE html>
<html lang="en">
<head>
<meta charset="utf-8">
<title>Brightway Electrical – Business Card</title>
<link rel="stylesheet" href="https://fonts.googleapis.com/css2?family=Barlow+Semi+Condensed:wght@600&family=Barlow:wght@400&display=swap">
<style>
  :root {
    --page-bg: #ffffff;
    --silver: #e3e6eb;
    --band-white: #ffffff;
    --emerald: #559a74;
    --mark-fill: #ffffff;
    --text-light: #ffffff;
  }
  * { margin: 0; padding: 0; box-sizing: border-box; }
  html, body {
    width: 1200px;
    height: 900px;
    overflow: hidden;
    background: var(--page-bg);
  }
  .business-card {
    position: absolute;
    left: 65px;
    top: 117px;
    width: 1075px;
    height: 648px;
    background: var(--emerald);
    overflow: hidden;
  }
  .card-top {
    position: absolute;
    left: 0; top: 0;
    width: 100%;
    height: 232px;
    background: var(--silver);
  }
  .name-band {
    position: absolute;
    left: 0; top: 232px;
    width: 100%;
    height: 58px;
    background: var(--band-white);
  }
  .company-word {
    position: absolute;
    top: 232px;
    height: 58px;
    display: flex;
    align-items: center;
    font-family: "Barlow Semi Condensed", Arial, sans-serif;
    font-weight: 600;
    font-size: 68px;
    line-height: 1;
    color: var(--emerald);
    text-transform: uppercase;
    white-space: nowrap;
  }
  .company-word--first {
    right: 740px;
    justify-content: flex-end;
  }
  .company-word--second {
    left: 603px;
  }
  .brand-square {
    position: absolute;
    left: 353px;
    top: 155px;
    width: 234px;
    height: 216px;
    background: var(--mark-fill);
    border-radius: 14px;
  }
  .contact-line {
    position: absolute;
    left: 0;
    top: 543px;
    width: 100%;
    text-align: center;
    font-family: "Barlow", Arial, sans-serif;
    font-weight: 400;
    font-size: 47px;
    line-height: 1;
    letter-spacing: 0.6px;
    color: var(--text-light);
    white-space: nowrap;
  }
</style>
</head>
<body>
  <div class="business-card">
    <div class="card-top"></div>
    <div class="name-band"></div>
    <span class="company-word company-word--first">Brightway</span>
    <div class="brand-square" aria-hidden="true"></div>
    <span class="company-word company-word--second">Electrical</span>
    <p class="contact-line">Tom Keller | EC 274381 | Mob: 0417 592 064</p>
  </div>
</body>
</html>
```